Simple and Approachable Cover for Pet Expo Company Page

Size: 2000 x 430; looking simply for words "Dunmore HR Consulting" and email address "DunmoreHRConsulting@brelvamail.com." This is for a cover photo for a company profile page for the Hollow Oak Expo, where I am a featured speaker on Employee Communications later this month. You can incorporate the attached photo to the left of the banner ad if you wish. The mood I wish to present is approachable, positive and simple.

Target Market(s)

small pet retail business owners

Industry/Entity Type

Pet Shop

Font styles to use
Serif
Sans Serif

Requirements
Must have
• Email address clearly defined/separated. Easy to read.
Nice to have
• I like the picture that I included; subtle pet paw background is also nice
Should not have
• No paid stock images

```html
<!DOCTYPE html>
<html lang="en">
<head>
<meta charset="utf-8">
<title>Dunmore HR Consulting – Cover Banner</title>
<link rel="stylesheet" href="https://fonts.googleapis.com/css2?family=Rubik:wght@600;700&family=Raleway:wght@600;700&display=swap">
<style>
  :root {
    --page-bg: #ffffff;
    --banner-yellow: #F6CD55;
    --band-light: #F3BE48;
    --band-orange: #EFAA3C;
    --ink-navy: #0B2D40;
    --rule-white: #ffffff;
    --photo-green: #7E9A5A;
    --photo-field: #A7B46E;
    --pet-orange: #E3A24E;
    --pet-cream: #F2E2C8;
  }
  html, body {
    margin: 0;
    width: 1200px;
    height: 1200px;
    overflow: hidden;
    background: var(--page-bg);
  }
  .canvas {
    position: relative;
    width: 1200px;
    height: 1200px;
  }
  .cover-banner {
    position: absolute;
    left: 29px;
    top: 477px;
    width: 1142px;
    height: 245px;
    background: var(--banner-yellow);
    overflow: hidden;
  }
  .banner-shapes {
    position: absolute;
    inset: 0;
  }
  .pet-photo {
    position: absolute;
    right: 0;
    top: 0;
    width: 152px;
    height: 245px;
    background: linear-gradient(160deg, var(--pet-orange) 0%, #D98E3C 45%, var(--pet-cream) 100%);
  }
  .brand-name {
    position: absolute;
    left: 496px;
    top: 46px;
    margin: 0;
    font-family: "Rubik", sans-serif;
    font-weight: 700;
    font-size: 74px;
    line-height: 1;
    letter-spacing: -1px;
    color: var(--ink-navy);
  }
  .brand-service {
    position: absolute;
    left: 544px;
    top: 127px;
    margin: 0;
    font-family: "Rubik", sans-serif;
    font-weight: 600;
    font-size: 47px;
    line-height: 1;
    color: var(--ink-navy);
  }
  .contact-email {
    position: absolute;
    left: 498px;
    top: 183px;
    display: flex;
    align-items: center;
    gap: 10px;
  }
  .contact-email svg { flex: none; }
  .contact-email a {
    font-family: "Raleway", sans-serif;
    font-weight: 700;
    font-size: 14.5px;
    letter-spacing: 1.4px;
    color: var(--ink-navy);
    text-decoration: none;
  }
</style>
</head>
<body>
<div class="canvas">
  <section class="cover-banner" aria-label="Dunmore HR Consulting cover">
    <svg class="banner-shapes" width="1142" height="245" viewBox="0 0 1142 245">
      <path class="band-light" d="M0 0 H378 Q450 122 378 245 H0 Z" fill="var(--band-light)"/>
      <path class="band-orange" d="M0 0 H347 Q410 122 347 245 H0 Z" fill="var(--band-orange)"/>
      <path class="owner-photo" role="img" aria-label="Photo of the consultants sitting on the grass with their two dogs in a park"
            d="M0 0 H313 Q385 122 313 245 H0 Z" fill="url(#photoTone)"/>
      <defs>
        <linearGradient id="photoTone" x1="0" y1="0" x2="0" y2="1">
          <stop offset="0" stop-color="var(--photo-green)"/>
          <stop offset="0.55" stop-color="var(--photo-field)"/>
          <stop offset="1" stop-color="#5C7AA6"/>
        </linearGradient>
      </defs>
      <line class="frame-rule" x1="515" y1="0" x2="515" y2="60" stroke="var(--rule-white)" stroke-width="2.5"/>
      <polyline class="frame-rule" points="871,155 929,155 929,245" fill="none" stroke="var(--rule-white)" stroke-width="2.5"/>
    </svg>

    <div class="pet-photo" role="img" aria-label="Photo of a smiling dog wearing a yellow knitted hat"></div>

    <h1 class="brand-name">Dunmore</h1>
    <p class="brand-service">HR Consulting</p>

    <div class="contact-email">
      <svg width="35" height="35" viewBox="0 0 35 35" aria-hidden="true">
        <circle cx="17.5" cy="17.5" r="16.5" fill="none" stroke="var(--ink-navy)" stroke-width="1.3"/>
        <rect x="8.5" y="11.5" width="18" height="12" rx="1.5" fill="none" stroke="var(--ink-navy)" stroke-width="1.3"/>
        <polyline points="8.5,12.5 17.5,19 26.5,12.5" fill="none" stroke="var(--ink-navy)" stroke-width="1.3"/>
      </svg>
      <a href="mailto:DunmoreHRConsulting@brelvamail.com">DunmoreHRConsulting@brelvamail.com</a>
    </div>
  </section>
</div>
</body>
</html>
```